Automotive parts Package (box) design

We are developing a new packaging concept for our automotive service and suspension parts line. I will share 2–3 sample designs—some from other brands and some AI‑generated—and we need a designer to create a unified, original design direction based on these references.

We already have an established brand name, KEM, along with a logo. The logo may be updated or redesigned, but the brand name KEM must remain.

- The project includes creating the full packaging design for our product boxes, developing or refining the logo if needed.

-Then, after choosing the design, we will apply the same design to 8 boxes with small customisation for each box to match the product.

- The box die-lines will be provided by us.

Attached are a few sample designs. We need you to develop three or more new designs in a similar style. If you have additional creative concepts beyond these references, you are welcome to include them. The only fixed requirement is that the brand name KEM must remain unchanged in all proposed designs.

Box files such as PNG, PDF (ready-to-print file) and Ai (Editable/ Source file) and fonts with 3D mockup images at the end of the project must be given to us.

Target Market(s)

Car spare parts shops

Industry/Entity Type

Auto Parts

Requirements
Must have
• Our brand name KEM
Nice to have
• Package similar to big auto parts suppliers such as PLW, VARNE

```html
<!DOCTYPE html>
<html lang="en">
<head>
<meta charset="utf-8">
<title>KEM Tie Rod-Ball Joint Box Dieline</title>
<link rel="stylesheet" href="https://fonts.googleapis.com/css2?family=Montserrat:wght@600;800;900&family=Roboto:wght@400;700&display=swap">
<style>
  :root {
    --kraft: #c39a6b;
    --kraft-dark: #a47c52;
    --brand-red: #c8000b;
    --band-black: #121212;
    --ink: #1a1a1a;
    --cut-line: #c0262d;
    --paper: #ffffff;
  }
  html, body {
    margin: 0;
    width: 1200px;
    height: 1155px;
    overflow: hidden;
    background: var(--paper);
  }
  .canvas {
    width: 1200px;
    height: 1155px;
    display: flex;
    align-items: center;
    justify-content: center;
  }
  .dieline { width: 1170px; height: auto; display: block; }
  .board { fill: var(--kraft); stroke: var(--cut-line); stroke-width: 0.9; }
  .fold { stroke: var(--kraft-dark); stroke-width: 0.6; fill: none; }
  .red { fill: var(--brand-red); }
  .band { fill: var(--band-black); }
  .brand-name { font-family: "Montserrat", sans-serif; font-weight: 900; fill: var(--ink); letter-spacing: 0.5px; }
  .brand-tag { font-family: "Montserrat", sans-serif; font-weight: 600; fill: var(--brand-red); font-size: 4.4px; letter-spacing: 0.2px; }
  .product-title { font-family: "Montserrat", sans-serif; font-weight: 800; fill: var(--ink); font-size: 11px; }
  .product-title.on-red { fill: #fff; }
  .cert { font-family: "Montserrat", sans-serif; font-weight: 800; fill: var(--ink); font-size: 5.5px; }
  .cert.on-red { fill: #fff; }
  .band-label { font-family: "Montserrat", sans-serif; font-weight: 800; fill: #fff; font-size: 8.5px; }
  .warranty-head { font-family: "Roboto", sans-serif; font-weight: 700; fill: var(--ink); font-size: 5px; }
  .warranty-copy { font-family: "Roboto", sans-serif; font-weight: 400; fill: var(--ink); font-size: 4.3px; }
  .shield { fill: var(--band-black); }
</style>
</head>
<body>
<main class="canvas">
<svg class="dieline" viewBox="10 432 918 442" xmlns="http://www.w3.org/2000/svg" aria-label="KEM tie rod-ball joint box, flat dieline">
  <defs>
    <clipPath id="body-clip"><rect x="47" y="595" width="873" height="190"/></clipPath>
    <clipPath id="lid-clip"><path d="M47 595 V452 Q47 440 59 440 H371 Q383 440 383 452 V595 Z"/></clipPath>
    <g id="warranty-shield">
      <path class="shield" d="M0 0 H18 V16 L9 22 L0 16 Z"/>
    </g>
  </defs>

  <!-- board pieces -->
  <path class="board glue-tab" d="M47 597 L17 606 V774 L47 783 Z"/>
  <path class="board lid" d="M47 595 V452 Q47 440 59 440 H371 Q383 440 383 452 V595 Z"/>
  <path class="board side-flap-top" d="M383 595 V515 H463 Q470 515 470 522 L473 570 L483 595 Z"/>
  <path class="board side-flap-top" d="M818 595 L828 570 L831 522 Q831 515 838 515 H920 V595 Z"/>
  <path class="board bottom-flap" d="M47 785 V835 H75 V858 Q75 865 82 865 H376 L383 856 V785 Z"/>
  <path class="board bottom-flap" d="M383 785 V835 H433 V858 Q433 865 440 865 H483 V785 Z"/>
  <path class="board bottom-flap" d="M483 785 L543 849 Q548 855 556 855 H770 Q778 855 782 849 L818 785 Z"/>
  <path class="board bottom-flap" d="M818 785 V865 H920 V785 Z"/>
  <rect class="board panels" x="47" y="595" width="873" height="190"/>

  <!-- lid artwork -->
  <g class="lid-art" clip-path="url(#lid-clip)">
    <polygon class="red" points="47,440 222,440 148,595 47,595"/>
    <line class="fold" x1="190" y1="495" x2="383" y2="495"/>
  </g>
  <g class="lid-text" transform="rotate(180 215 517)">
    <text class="band-label" x="292" y="536" font-size="7">SUSPENSION PARTS</text>
    <text class="product-title on-red" x="315" y="550">TIE</text>
    <text class="product-title on-red" x="315" y="561">ROD-BALL</text>
    <text class="product-title on-red" x="315" y="572">JOINT</text>
    <text class="cert on-red" x="315" y="580">ISO 9001</text>
    <text class="brand-name" x="56" y="467" font-size="20">KEM</text>
    <text class="brand-tag" x="56" y="474">AUTOMOTIVE COMPONENTS</text>
    <use href="#warranty-shield" x="60" y="493"/>
    <circle class="red" cx="93" cy="503" r="7"/>
  </g>

  <!-- body artwork -->
  <g class="body-art" clip-path="url(#body-clip)">
    <!-- front panel -->
    <polygon class="red" points="238,595 410,595 300,785 118,785"/>
    <polygon class="band" points="47,735 485,735 462,772 47,772"/>
    <polygon class="red" points="328,735 340,735 318,772 306,772"/>
    <polygon class="red" points="348,735 360,735 338,772 326,772"/>
    <polygon class="red" points="368,735 380,735 358,772 346,772"/>
    <polygon class="red" points="408,735 420,735 398,772 386,772"/>
    <polygon class="red" points="428,735 440,735 418,772 406,772"/>
    <polygon class="red" points="448,735 460,735 438,772 426,772"/>
    <!-- back panel -->
    <polygon class="red" points="680,595 845,595 735,785 552,785"/>
    <polygon class="band" points="483,735 790,735 768,772 483,772"/>
    <polygon class="red" points="760,735 772,735 750,772 738,772"/>
    <polygon class="red" points="780,735 792,735 770,772 758,772"/>
    <polygon class="red" points="800,735 840,735 818,772 778,772"/>
    <!-- fold lines -->
    <line class="fold" x1="383" y1="595" x2="383" y2="785"/>
    <line class="fold" x1="483" y1="595" x2="483" y2="785"/>
    <line class="fold" x1="818" y1="595" x2="818" y2="785"/>
  </g>

  <!-- front panel text -->
  <g class="front-panel">
    <text class="brand-name" x="60" y="621" font-size="20">KEM</text>
    <text class="brand-tag" x="60" y="629">AUTOMOTIVE COMPONENTS</text>
    <text class="product-title" x="60" y="652">TIE</text>
    <text class="product-title" x="60" y="664">ROD-BALL</text>
    <text class="product-title" x="60" y="676">JOINT</text>
    <text class="cert" x="60" y="684">ISO 9001</text>
    <use href="#warranty-shield" x="60" y="694"/>
    <circle class="red" cx="93" cy="704" r="7"/>
    <text class="band-label" x="245" y="757" text-anchor="middle">SUSPENSION PARTS</text>
  </g>

  <!-- side panel -->
  <g class="side-panel">
    <text class="brand-name" x="433" y="717" font-size="22" text-anchor="middle">KEM</text>
    <text class="brand-tag" x="433" y="725" text-anchor="middle">AUTOMOTIVE COMPONENTS</text>
  </g>

  <!-- back panel text -->
  <g class="back-panel">
    <text class="brand-name" x="495" y="621" font-size="20">KEM</text>
    <text class="brand-tag" x="495" y="629">AUTOMOTIVE COMPONENTS</text>
    <text class="product-title" x="495" y="652">TIE</text>
    <text class="product-title" x="495" y="664">ROD-BALL</text>
    <text class="product-title" x="495" y="676">JOINT</text>
    <text class="cert" x="495" y="684">ISO 9001</text>
    <use href="#warranty-shield" x="495" y="694"/>
    <circle class="red" cx="528" cy="704" r="7"/>
    <text class="band-label" x="662" y="757" text-anchor="middle">SUSPENSION PARTS</text>
  </g>

  <!-- warranty side panel -->
  <g class="warranty-panel" text-anchor="end">
    <text class="warranty-head" x="912" y="611">KEM WARRANTY</text>
    <text class="warranty-copy" x="912" y="619">(Manufacturing Defect Only)</text>
    <text class="warranty-copy" x="912" y="634">KEM suspension parts are</text>
    <text class="warranty-copy" x="912" y="640">covered for manufacturing</text>
    <text class="warranty-copy" x="912" y="646">defects for 6 months from</text>
    <text class="warranty-copy" x="912" y="652">purchase.</text>
    <text class="warranty-copy" x="912" y="664">Coverage includes defects in</text>
    <text class="warranty-copy" x="912" y="670">materials only.</text>
    <text class="warranty-copy" x="912" y="682">This warranty does not cover</text>
    <text class="warranty-copy" x="912" y="688">improper installation, misuse,</text>
    <text class="warranty-copy" x="912" y="694">accidents, wear and tear, or</text>
    <text class="warranty-copy" x="912" y="700">use in racing/off-road</text>
    <text class="warranty-copy" x="912" y="706">conditions.</text>
    <text class="warranty-copy" x="912" y="718">Approved claims are resolved</text>
    <text class="warranty-copy" x="912" y="724">by replacement of the part</text>
    <text class="warranty-copy" x="912" y="730">only.</text>
    <text class="warranty-copy" x="912" y="742">Invoice and defective part</text>
    <text class="warranty-copy" x="912" y="748">must be provided for</text>
    <text class="warranty-copy" x="912" y="754">inspection.</text>
  </g>
  <use href="#warranty-shield" x="860" y="757"/>
  <circle class="red" cx="894" cy="767" r="7"/>
</svg>
</main>
</body>
</html>
```